Rock, Paper Scissors Championship Flyer

We need a dynamic, bold and exciting flyer to promote the following event at our sports center. The event will be primarily focused for adults, but children are welcome to join

Rock, Paper, Scissors Championship - $$$ prizes
Date: June 9th, 2018
Time: 11am-4pm
Fee: $2 to enter, free for spectators
Heats to determine the overall ‘Rock, Paper, Scissors’ champion!
- Cash prizes on offer
- Live music.
- Food and beverage available for purchase

Belvorrow Sports Center, Roselle NJ
908-555-3162
www.belvorrowgrounds.example

Must include our logo (does not have to be huge) and County seal (both attached)

Colors

Designer to choose colors to be used in the design.

Requirements
Must have
• Should be fun and colorful
• The following info and attached logos:
• Rock, Paper, Scissors Championship - $$$ prizes
• Date: June 9th, 2018
• Time: 11am-4pm
• Fee: $2 to enter, free for spectators
• Heats to determine the overall ‘Rock, Paper, Scissors’ champion!
• - Cash prizes on offer
• - Live music.
• - Food and beverage available for purchase
• Belvorrow Sports Center, Roselle NJ
• 908-555-3162
• www.belvorrowgrounds.example
Nice to have
• There are a few inspirational photos attached to give an idea of what we are looking for.

```html
<!DOCTYPE html>
<html lang="en">
<head>
<meta charset="utf-8">
<title>Rock, Paper, Scissors Championship</title>
<link href="https://fonts.googleapis.com/css2?family=Kaushan+Script&family=Roboto:wght@400;500;700&display=swap" rel="stylesheet">
<style>
  :root {
    --party-dark: #2a1036;
    --party-magenta: #a2306e;
    --party-amber: #d98a52;
    --teal-deep: #1fa3a0;
    --teal-mid: #5fd0c2;
    --mint-light: #c9f0dc;
    --lime-glow: #e6f7b8;
    --banner-red: #c8141c;
    --banner-red-dark: #8e0d12;
    --navy: #173f66;
    --navy-dark: #0f2c4a;
    --ink: #10283f;
    --white: #ffffff;
    --photo-frame: #ffffff;
  }
  * { box-sizing: border-box; margin: 0; padding: 0; }
  html, body { width: 848px; height: 1200px; overflow: hidden; background: #e8e8e8; }
  .flyer {
    position: relative; width: 848px; height: 1200px; overflow: hidden;
    font-family: "Roboto", Arial, sans-serif;
    background:
      linear-gradient(100deg, transparent 0 30%, rgba(255,255,255,.18) 31%, transparent 38%),
      linear-gradient(172deg, var(--teal-deep) 0%, var(--teal-mid) 40%, var(--mint-light) 62%, var(--lime-glow) 78%, var(--teal-mid) 100%);
  }
  .hero-photo {
    position: absolute; left: 0; top: 0; width: 848px; height: 560px;
    background:
      radial-gradient(ellipse at 20% 15%, rgba(255,120,200,.55), transparent 45%),
      radial-gradient(ellipse at 80% 20%, rgba(120,160,255,.45), transparent 45%),
      radial-gradient(ellipse at 55% 55%, var(--party-amber), transparent 55%),
      linear-gradient(180deg, var(--party-dark) 0%, var(--party-magenta) 55%, rgba(95,208,194,0) 100%);
  }
  .title {
    position: absolute; left: 0; width: 848px; text-align: center;
    font-family: "Kaushan Script", cursive; color: var(--white);
    text-shadow: 2px 3px 4px rgba(0,0,0,.55);
  }
  .title-main { top: 28px; font-size: 44px; }
  .title-prizes { top: 96px; font-size: 56px; }
  .inset-photo {
    position: absolute; border: 3px solid var(--photo-frame);
    box-shadow: 0 4px 10px rgba(0,0,0,.35);
  }
  .inset-picnic { left: 21px; top: 378px; width: 264px; height: 171px; background: linear-gradient(160deg, #8fae5a, #d6a66b 60%, #7b5a3a); }
  .inset-singer { left: 292px; top: 420px; width: 264px; height: 172px; background: linear-gradient(135deg, #f4f4f4, #d9d2cf 55%, #b8263a); }
  .inset-runners { left: 563px; top: 485px; width: 263px; height: 170px; background: linear-gradient(170deg, #5f8f3c, #a8c776 55%, #c7b790); }
  .highlights { position: absolute; left: 31px; top: 608px; list-style: none; }
  .highlights li { font-size: 24px; color: var(--ink); line-height: 40px; padding-left: 24px; position: relative; }
  .highlights li::before { content: ""; position: absolute; left: 2px; top: 17px; width: 8px; height: 8px; border-radius: 50%; background: var(--white); }
  .date-banner {
    position: absolute; left: 97px; top: 738px; width: 690px; height: 128px;
    background: linear-gradient(180deg, var(--banner-red) 0%, var(--banner-red-dark) 100%);
    border-top: 10px solid var(--navy-dark); text-align: center; color: var(--white);
    box-shadow: 0 6px 10px rgba(0,0,0,.3);
  }
  .date-line { font-size: 50px; font-weight: 500; margin-top: 10px; line-height: 58px; }
  .time-line { font-size: 35px; font-weight: 500; line-height: 42px; }
  .fee-box {
    position: absolute; left: 103px; top: 874px; width: 678px; height: 68px;
    background: var(--navy); color: var(--white); font-size: 35px; font-weight: 500;
    display: flex; align-items: center; justify-content: center;
  }
  .heats { position: absolute; left: 0; width: 848px; top: 968px; text-align: center; font-size: 24px; font-weight: 500; color: var(--ink); }
  .county-seal { position: absolute; left: 10px; top: 1040px; width: 152px; height: 152px; border-radius: 50%; background: #2f5a8a; border: 6px solid #e7c66b; }
  .contact { position: absolute; left: 190px; top: 1052px; width: 470px; text-align: center; color: var(--ink); }
  .contact-address { font-size: 24px; font-weight: 500; }
  .contact-phone { font-size: 40px; font-weight: 500; margin-top: 4px; display: flex; align-items: center; justify-content: center; gap: 8px; }
  .contact-web { font-size: 23px; font-weight: 500; margin-top: 2px; }
  .center-name { position: absolute; left: 672px; top: 1078px; width: 165px; text-align: center; color: var(--navy); font-size: 19px; font-weight: 700; line-height: 24px; }
  .center-name .mark { display: block; width: 34px; height: 34px; border-radius: 50%; background: var(--navy); margin: 0 auto 8px; }
</style>
</head>
<body>
<div class="flyer">
  <div class="hero-photo" role="img" aria-label="Photo of young women dancing and cheering at a party under colourful lights"></div>
  <div class="title title-main">Rock, Paper, Scissors Championship</div>
  <div class="title title-prizes">$$$ prizes</div>

  <div class="inset-photo inset-picnic" role="img" aria-label="Photo of friends sharing food and drinks at an outdoor table"></div>
  <div class="inset-photo inset-singer" role="img" aria-label="Photo of a singer holding a microphone"></div>
  <div class="inset-photo inset-runners" role="img" aria-label="Photo of two people jogging along a park path"></div>

  <ul class="highlights">
    <li>Cash prizes on offer</li>
    <li>Live music.</li>
    <li>Food and beverage available for purchase</li>
  </ul>

  <div class="date-banner">
    <div class="date-line">Date: June 9th, 2018</div>
    <div class="time-line">Time: 11am-4pm</div>
  </div>
  <div class="fee-box">Fee: $2 to enter, free for spectators</div>

  <p class="heats">Heats to determine the overall ‘Rock, Paper, Scissors’ champion!</p>

  <div class="county-seal" role="img" aria-label="County seal"></div>

  <div class="contact">
    <div class="contact-address">Belvorrow Sports Center, Roselle NJ</div>
    <div class="contact-phone">
      <svg width="34" height="34" viewBox="0 0 24 24" aria-hidden="true"><path fill="#10283f" d="M6.6 10.8c1.4 2.8 3.8 5.1 6.6 6.6l2.2-2.2c.3-.3.7-.4 1-.2 1.1.4 2.3.6 3.6.6.6 0 1 .4 1 1V20c0 .6-.4 1-1 1C10.6 21 3 13.4 3 4c0-.6.4-1 1-1h3.5c.6 0 1 .4 1 1 0 1.3.2 2.5.6 3.6.1.3 0 .7-.2 1z"/></svg>
      908-555-3162
    </div>
    <div class="contact-web">www.belvorrowgrounds.example</div>
  </div>

  <div class="center-name"><span class="mark"></span>Belvorrow Sports Center</div>
</div>
</body>
</html>
```